Harrow's Electrical & Solar - Business Cards

I want my business card to stand out from the rest. I will provide my business name logo and my icon logo to be implemented onto the card.

On the front of the card, can i have the following. Just make it neat & professional please.

Liam Corbett
harrowselectrical@quillmail.test
0438 917 605
ABN: 41 602 719 384
License No. 582164K
FREE QUOTES
24/7 Emergency

On the back of the card, can I have "Our Services" and maybe add the S logo on the back in the background or something. Under "Our Services" I want the following:

LED Lighting Upgrades
Switches & Outlets
Smoke Alarms
Switchboard Upgrades
Fault Finding
Rewiring
New Builds
Test & Tagging
All Electrical Maintenance & Repairs

Can you guys add the instagram logo and next to it, put harrows_electrical

Can you guys also add the facebook logo and next to it put Harrow's Electrical & Solar. Make sure the instagram & facebook icon is in either white, green or black.

Also I have put down double sided, not sure why when i save it, it keeps going to single sided. I need my business card double sided.

Target Market(s)

New Customers

Contact Information for Business Card

Liam Corbett harrowselectrical@quillmail.test 0438 917 605 ABN: 41 602 719 384 License No. 582164K FREE QUOTES 24/7 Emergency

Requirements
Must have
• must be tidy, professional and appealing

```html
<!DOCTYPE html>
<html lang="en">
<head>
<meta charset="utf-8">
<title>Harrow's Electrical &amp; Solar – Business Cards</title>
<link rel="stylesheet" href="https://fonts.googleapis.com/css2?family=Michroma&family=Poppins:wght@400;500;600&family=Saira+Condensed:ital,wght@1,800&display=swap">
<style>
  :root {
    --bg: #ffffff;
    --card: #0b0b0b;
    --card-mid: #1a1a1a;
    --green: #3ab54a;
    --green-dark: #1f7a2c;
    --silver: #c9ccce;
    --silver-light: #eef0f1;
    --silver-dark: #8e9295;
    --text-light: #d8d8d8;
    --ink: #111111;
  }
  html, body {
    margin: 0;
    width: 1200px;
    height: 1200px;
    overflow: hidden;
    background: var(--bg);
  }
  .card {
    position: absolute;
    left: 196px;
    width: 807px;
    height: 474px;
    display: block;
    box-shadow: 0 4px 10px rgba(0,0,0,0.35);
  }
  .card--front { top: 90px; }
  .card--back { top: 622px; }
  .heading { font-family: "Michroma", sans-serif; }
  .body { font-family: "Poppins", sans-serif; }
  .display { font-family: "Saira Condensed", sans-serif; font-style: italic; font-weight: 800; }
</style>
</head>
<body>

<!-- Front side -->
<svg class="card card--front" viewBox="0 0 673 395" role="group" aria-label="Business card front">
  <defs>
    <radialGradient id="card-glow" cx="0.35" cy="0.5" r="0.8">
      <stop offset="0" stop-color="var(--card-mid)"/>
      <stop offset="1" stop-color="var(--card)"/>
    </radialGradient>
    <linearGradient id="silver-fill" x1="0" y1="0" x2="0" y2="1">
      <stop offset="0" stop-color="var(--silver-light)"/>
      <stop offset="1" stop-color="var(--silver-dark)"/>
    </linearGradient>
    <clipPath id="front-clip"><rect width="673" height="395"/></clipPath>
  </defs>
  <g clip-path="url(#front-clip)">
    <rect class="card-base" width="673" height="395" fill="url(#card-glow)"/>
    <!-- faint decorative ring -->
    <circle class="deco-ring" cx="552" cy="105" r="122" fill="none" stroke="#1d2a1f" stroke-width="8"/>
    <!-- top silver tab -->
    <polygon class="top-tab" points="50,0 227,0 212,22 65,22" fill="url(#silver-fill)"/>
    <!-- wordmark -->
    <text class="heading wordmark" x="48" y="90" font-size="40" fill="var(--silver)">HARROW'S</text>
    <text class="heading wordmark-sub" x="84" y="120" font-size="12.5" fill="var(--silver)" letter-spacing="3">ELECTRICAL &amp; SOLAR</text>

    <!-- name -->
    <text class="heading person-name" x="45" y="236" font-size="19" fill="var(--green)" letter-spacing="1">LIAM CORBETT</text>
    <line class="divider" x1="45" y1="248" x2="630" y2="248" stroke="#6b6b6b" stroke-width="1"/>

    <!-- contact icons -->
    <g class="contact-icons" fill="var(--green)" stroke="var(--green)">
      <path d="M48 262 q-1 6 5 10 l2-2 -2-3 -2 1 q-2-2-2-4 l1-1 -2-3z" stroke="none"/>
      <rect x="47" y="285" width="10" height="7" fill="none" stroke-width="1.2"/>
      <path d="M47 285 l5 4 5-4" fill="none" stroke-width="1.2"/>
      <polygon points="54,306 47,314 52,314 49,321 57,312 52,312" stroke="none"/>
      <polygon points="54,327 47,335 52,335 49,342 57,333 52,333" stroke="none"/>
    </g>
    <line class="contact-rule" x1="69" y1="258" x2="69" y2="345" stroke="#777" stroke-width="1"/>

    <text class="body contact-phone" x="79" y="273" font-size="14.5" font-weight="600" fill="var(--text-light)">0438 917 605</text>
    <text class="body contact-email" x="79" y="294" font-size="13.5" fill="#bdbdbd">harrowselectrical@quillmail.test</text>
    <text class="body contact-abn" x="79" y="318" font-size="13.5"><tspan fill="var(--green)">ABN:</tspan><tspan fill="var(--text-light)"> 41 602 719 384</tspan></text>
    <text class="body contact-license" x="79" y="339" font-size="13.5"><tspan fill="var(--green)">License No.</tspan><tspan fill="var(--text-light)"> 582164K</tspan></text>

    <!-- emergency badge -->
    <g class="emergency-badge">
      <text class="display" x="480" y="352" font-size="72" fill="var(--green)">2</text>
      <text class="display" x="508" y="358" font-size="72" fill="url(#silver-fill)">4</text>
      <text class="display" x="552" y="300" font-size="34" fill="var(--green)">X7</text>
      <text class="display" x="552" y="325" font-size="17" fill="var(--silver)">EMERGENCY</text>
      <text class="display" x="552" y="348" font-size="25" fill="var(--green)">SERVICE</text>
    </g>

    <!-- bottom band -->
    <rect class="bottom-band" x="0" y="378" width="673" height="17" fill="var(--green)"/>
    <polygon class="quotes-tab" points="267,378 285,353 440,353 458,378" fill="var(--green)"/>
    <polygon class="accent-line" points="458,372 650,372 660,380 458,380" fill="var(--green-dark)"/>
    <text class="heading quotes-label" x="363" y="370" font-size="12" fill="var(--ink)" text-anchor="middle" letter-spacing="1">FREE QUOTES</text>
  </g>
</svg>

<!-- Back side -->
<svg class="card card--back" viewBox="0 0 673 395" role="group" aria-label="Business card back">
  <defs>
    <linearGradient id="band-fill" x1="0" y1="0" x2="1" y2="0">
      <stop offset="0" stop-color="var(--silver)"/>
      <stop offset="0.5" stop-color="var(--silver-light)"/>
      <stop offset="1" stop-color="var(--silver-dark)"/>
    </linearGradient>
    <clipPath id="back-clip"><rect width="673" height="395"/></clipPath>
  </defs>
  <g clip-path="url(#back-clip)">
    <rect class="card-base" width="673" height="395" fill="var(--card)"/>
    <!-- social band -->
    <rect class="social-band" x="0" y="309" width="673" height="86" fill="url(#band-fill)"/>
    <!-- decorative ring -->
    <circle class="deco-ring" cx="527" cy="203" r="160" fill="var(--card)" stroke="var(--green)" stroke-width="12"/>

    <text class="heading services-title" x="45" y="52" font-size="21" fill="var(--green)" letter-spacing="1">OUR SERVICES</text>
    <g class="services-list body" font-size="14.5" fill="var(--text-light)">
      <g class="bolts" fill="var(--green)">
        <polygon points="54,70 47,78 52,78 49,84 57,76 52,76"/>
        <polygon points="54,95 47,103 52,103 49,109 57,101 52,101"/>
        <polygon points="54,120 47,128 52,128 49,134 57,126 52,126"/>
        <polygon points="54,145 47,153 52,153 49,159 57,151 52,151"/>
        <polygon points="54,170 47,178 52,178 49,184 57,176 52,176"/>
        <polygon points="54,195 47,203 52,203 49,209 57,201 52,201"/>
        <polygon points="54,220 47,228 52,228 49,234 57,226 52,226"/>
        <polygon points="54,245 47,253 52,253 49,259 57,251 52,251"/>
        <polygon points="54,270 47,278 52,278 49,284 57,276 52,276"/>
      </g>
      <text x="66" y="82">LED Lighting Upgrades</text>
      <text x="66" y="107">Switches &amp; Outlets</text>
      <text x="66" y="132">Smoke Alarms</text>
      <text x="66" y="157">Switchboard Upgrades</text>
      <text x="66" y="182">Fault Finding</text>
      <text x="66" y="207">Rewiring</text>
      <text x="66" y="232">New Builds</text>
      <text x="66" y="257">Test &amp; Tagging</text>
      <text x="66" y="282">All Electrical Maintenance &amp; Repairs</text>
    </g>

    <!-- social handles -->
    <g class="social">
      <circle cx="114" cy="337" r="13" fill="var(--ink)"/>
      <text class="body" x="114" y="371" font-size="13.5" font-weight="500" fill="var(--ink)" text-anchor="middle">harrows_electrical</text>
      <line x1="199" y1="320" x2="199" y2="380" stroke="#555" stroke-width="1"/>
      <circle cx="312" cy="337" r="13" fill="var(--ink)"/>
      <text class="body" x="312" y="371" font-size="13.5" font-weight="500" fill="var(--ink)" text-anchor="middle">Harrow's Electrical &amp; Solar</text>
    </g>
  </g>
</svg>

</body>
</html>
```